Elegant, Playful, Health And Wellness Packaging Design for an Essential Oil Diffuser

Box design for diffuser, should be elegant, luxury, white box with gold foil and vibrant color combination that pops off the white box.

Designs look the same

```html
<!DOCTYPE html>
<html lang="en">
<head>
<meta charset="utf-8">
<title>Velara Luma Diffuser – Box Dieline</title>
<link rel="stylesheet" href="https://fonts.googleapis.com/css2?family=Montserrat:wght@500;600;700;800&family=Oswald:wght@700&display=swap">
<style>
  :root {
    --backdrop: #116e7a;
    --cocoa: #2d1a17;
    --cocoa-weave: #3b2723;
    --aqua: #1ec8e4;
    --paper: #ffffff;
    --silver-weave: #d9d9d9;
    --ink: #2d1a17;
    --window-edge: #d4d4d4;
  }
  html, body {
    margin: 0;
    padding: 0;
    width: 1200px;
    height: 1200px;
    overflow: hidden;
    background: var(--backdrop);
  }
  .dieline {
    display: block;
    width: 1200px;
    height: 1200px;
    font-family: "Montserrat", sans-serif;
  }
  .panel-paper { fill: var(--paper); }
  .panel-cocoa { fill: var(--cocoa); }
  .weave-light { fill: var(--silver-weave); }
  .weave-dark { fill: var(--cocoa-weave); }
  .rule-band { fill: var(--cocoa); }
  .tagline { fill: var(--aqua); font-size: 15px; font-weight: 600; letter-spacing: 0.5px; text-anchor: middle; }
  .brand-aqua { fill: var(--aqua); font-weight: 800; letter-spacing: 2px; text-anchor: middle; }
  .brand-ink { fill: var(--ink); font-weight: 800; letter-spacing: 2px; text-anchor: middle; }
  .brand-dot-aqua { fill: none; stroke: var(--aqua); stroke-width: 6; }
  .brand-dot-ink { fill: none; stroke: var(--ink); stroke-width: 5; }
  .product-name { fill: var(--ink); font-family: "Oswald", sans-serif; font-weight: 700; font-size: 50px; text-anchor: middle; }
  .collection { fill: var(--ink); font-size: 12.5px; font-weight: 500; letter-spacing: 0.4px; text-anchor: middle; }
  .web-address { fill: var(--aqua); font-size: 19px; font-weight: 600; text-anchor: middle; }
  .window { fill: url(#windowShade); stroke: var(--window-edge); stroke-width: 3; }
  .info-title { fill: var(--ink); font-size: 9.5px; font-weight: 700; }
  .info-copy { fill: var(--ink); font-size: 8.6px; font-weight: 500; }
  .info-tag { fill: var(--cocoa); }
  .info-tag-text { fill: var(--paper); font-size: 8.5px; font-weight: 700; text-anchor: middle; }
</style>
</head>
<body>
<svg class="dieline" viewBox="115 485 1700 1700" xmlns="http://www.w3.org/2000/svg">
  <defs>
    <radialGradient id="windowShade" cx="50%" cy="45%" r="55%">
      <stop offset="0%" stop-color="#ffffff" stop-opacity="0.05"/>
      <stop offset="80%" stop-color="#ffffff" stop-opacity="0.12"/>
      <stop offset="100%" stop-color="#9a9a9a" stop-opacity="0.45"/>
    </radialGradient>
  </defs>

  <!-- Left side panel -->
  <g class="side-panel-info">
    <path class="panel-paper" d="M140,1250 L190,1080 Q196,1062 215,1062 L520,1062 Q538,1062 541,1080 L553,1250 Z"/>
    <rect class="panel-paper" x="140" y="1250" width="413" height="345"/>
    <rect class="rule-band" x="140" y="1270" width="413" height="10"/>
    <rect class="weave-light" x="140" y="1280" width="413" height="315" role="img" aria-label="Light grey woven wave pattern"/>
    <path class="panel-paper" d="M140,1595 L553,1595 L553,1690 L365,1690 Q347,1690 347,1708 L347,1790 Q347,1800 337,1800 L150,1800 Q140,1800 140,1790 Z"/>

    <circle class="brand-dot-ink" cx="346" cy="1340" r="28"/>
    <text class="brand-ink" x="346" y="1392" font-size="20">VELARA</text>

    <text class="info-title" x="190" y="1420">VELARA RARE ESSENTIAL OILS DIFFUSER</text>
    <text class="info-copy" x="190" y="1431">Experience the pure essence of nature with the Rare Oils Luma Diffuser.</text>
    <text class="info-copy" x="190" y="1441">Sourced from the farthest reaches of the earth, Velara Rare Oils are</text>
    <text class="info-copy" x="190" y="1451">extracted only from the highest quality and purest raw form ingredients.</text>
    <text class="info-copy" x="190" y="1461">Using the Luma diffuser with Velara Rare Oils can help improve health,</text>
    <text class="info-copy" x="190" y="1471">quality of life, and overall spiritual balance.</text>

    <rect class="info-tag" x="190" y="1492" width="72" height="12"/>
    <text class="info-tag-text" x="226" y="1501">FEATURES</text>
    <text class="info-copy" x="190" y="1517">• Continuous diffusing</text>
    <text class="info-copy" x="190" y="1527">• Timer settings</text>
    <text class="info-copy" x="190" y="1537">• 7 LED color &amp; light settings</text>
    <text class="info-copy" x="190" y="1547">• Portable</text>
    <text class="info-copy" x="190" y="1557">• Pet safe</text>
    <text class="info-copy" x="190" y="1567">• Easy to clean</text>

    <rect class="info-tag" x="360" y="1492" width="100" height="12"/>
    <text class="info-tag-text" x="410" y="1501">SPECIFICATIONS</text>
    <text class="info-copy" x="360" y="1517">• Dimensions: 135*135*108mm</text>
    <text class="info-copy" x="360" y="1527">• Capacity: 300ml</text>
    <text class="info-copy" x="360" y="1537">• 33 ml/hour output</text>
    <text class="info-copy" x="360" y="1547">• Safety Auto-off when empty</text>
    <text class="info-copy" x="360" y="1557">• Whisper Quiet</text>
    <text class="info-copy" x="360" y="1567">• Contains 1 Luma Diffuser, 1 Power</text>
    <text class="info-copy" x="367" y="1577">Adaptor</text>
  </g>

  <!-- Front panel with lid -->
  <g class="front-panel">
    <rect class="panel-paper" x="553" y="1270" width="412" height="325"/>
    <path class="panel-cocoa" d="M553,832 Q553,812 573,812 L945,812 Q965,812 965,832 L965,1535 L915,1452 Q908,1440 893,1440 L612,1440 Q599,1440 595,1428 L553,1282 Z"/>
    <path class="panel-paper" d="M553,1595 L965,1595 L965,1850 Q965,1860 955,1860 L875,1860 Q865,1860 865,1850 L865,1800 L665,1800 L665,1850 Q665,1860 655,1860 L563,1860 Q553,1860 553,1850 Z"/>

    <g class="lid-brand" transform="rotate(180 760 1030)">
      <text class="brand-aqua" x="760" y="1100" font-size="44">VELARA</text>
      <circle class="brand-dot-aqua" cx="760" cy="990" r="70"/>
    </g>

    <text class="tagline" x="760" y="1300">EXPERIENCE THE ESSENCE OF NATURE</text>
    <circle class="window" cx="760" cy="1432" r="112"/>
    <circle class="brand-dot-aqua" cx="760" cy="1368" r="28" stroke-width="4"/>
    <text class="brand-aqua" x="760" y="1418" font-size="17">VELARA</text>
    <text class="product-name" x="760" y="1508">LUMA</text>
    <text class="collection" x="760" y="1564">SIGNATURE RARE OILS COLLECTION</text>
    <text class="collection" x="760" y="1580">ULTRASONIC DIFFUSER</text>
  </g>

  <!-- Right side panel -->
  <g class="side-panel-web">
    <path class="panel-paper" d="M965,1270 L975,1085 Q978,1062 1000,1062 L1310,1062 Q1325,1062 1332,1080 L1378,1240 L1378,1270 Z"/>
    <rect class="weave-dark" x="965" y="1270" width="413" height="268" role="img" aria-label="Dark cocoa woven wave pattern"/>
    <rect class="panel-paper" x="965" y="1538" width="413" height="57"/>
    <path class="panel-paper" d="M965,1595 L1378,1595 L1378,1790 Q1378,1800 1368,1800 L1190,1800 Q1172,1800 1172,1782 L1172,1690 L965,1690 Z"/>

    <circle class="brand-dot-aqua" cx="1172" cy="1386" r="30" stroke-width="4"/>
    <text class="brand-aqua" x="1172" y="1437" font-size="19">VELARA</text>
    <text class="web-address" x="1172" y="1458">www.velara-oils.com</text>
  </g>

  <!-- Back panel -->
  <g class="back-panel">
    <rect class="panel-cocoa" x="1524" y="1223" width="120" height="55" rx="8"/>
    <rect class="panel-paper" x="1378" y="1270" width="412" height="325"/>
    <path class="panel-cocoa" d="M1378,1270 L1790,1270 L1750,1428 Q1745,1442 1730,1442 L1442,1442 Q1427,1442 1420,1455 L1378,1532 Z"/>
    <path class="panel-paper" d="M1378,1595 L1790,1595 L1688,1800 L1688,1850 Q1688,1860 1678,1860 L1492,1860 Q1482,1860 1482,1850 L1482,1800 Z"/>

    <text class="tagline" x="1584" y="1300">EXPERIENCE THE ESSENCE OF NATURE</text>
    <circle class="window" cx="1584" cy="1432" r="112"/>
    <circle class="brand-dot-aqua" cx="1584" cy="1368" r="28" stroke-width="4"/>
    <text class="brand-aqua" x="1584" y="1418" font-size="17">VELARA</text>
    <text class="product-name" x="1584" y="1508">LUMA</text>
    <text class="collection" x="1584" y="1564">SIGNATURE RARE OILS COLLECTION</text>
    <text class="collection" x="1584" y="1580">ULTRASONIC DIFFUSER</text>
  </g>
</svg>
</body>
</html>
```